Cocktail Bar Aperitivo Promotion

I need a flyer designed for my aperitivo promotion. Aperitivo is an Italian tradition much like the cocktail hour where you can relax and unwind over a drink and a little snack.
Bramble Toots a unique and fun 1950’s style bar - a relaxed local meeting place, the kind of bar where your bartender drinks on their night off. The final design should reflect the enthusiastic spirit of the 1950s cocktail culture as well as the fun, summery Italian vibe of the aperitvo and it needs to highlight the 2 aperitivo cocktails on offer, their price and the time of the promotion. Please also include the logo, address, phone number and website.
Negronis $16
Vellaro Spritz $14
All share plates $10
From 4pm - 6pm every day
Address: 472 Wexcombe Rd Wexcombe
Phone: 8153 2947
brambletoots.com.au
Please also refer to our website- brambletoots.com.au for a sense of who we are and what we do.

```html
<!DOCTYPE html>
<html lang="en">
<head>
<meta charset="utf-8">
<title>Bramble Toots – Aperitivo</title>
<link rel="stylesheet" href="https://fonts.googleapis.com/css2?family=Kaushan+Script&family=Raleway:wght@400;500&display=swap">
<style>
  :root {
    --peach: #f9d38f;
    --paper: #ffffff;
    --ink: #111111;
    --glass-top: #a0347a;
    --glass-mid: #c42a55;
    --glass-base: #e0232b;
  }
  * { margin: 0; padding: 0; box-sizing: border-box; }
  html, body { width: 848px; height: 1200px; overflow: hidden; background: var(--paper); }
  .flyer {
    position: relative;
    width: 848px;
    height: 1200px;
    overflow: hidden;
    background: var(--paper);
    color: var(--ink);
    font-family: "Kaushan Script", cursive;
  }
  .backdrop { position: absolute; inset: 0; }
  .brand {
    position: absolute;
    top: 22px;
    left: 0;
    width: 848px;
    text-align: center;
    font-size: 34px;
    line-height: 50px;
  }
  .rule {
    position: absolute;
    left: 93px;
    width: 662px;
    height: 3px;
    background: var(--ink);
  }
  .rule--top { top: 131px; }
  .rule--bottom { top: 327px; }
  .title {
    position: absolute;
    top: 128px;
    left: 0;
    width: 848px;
    text-align: center;
    font-size: 150px;
    line-height: 200px;
    font-weight: 400;
  }
  .hours {
    position: absolute;
    top: 332px;
    right: 108px;
    font-size: 34px;
    line-height: 48px;
  }
  .cocktail-art {
    position: absolute;
    left: 402px;
    top: 428px;
    width: 352px;
    height: 618px;
    border-radius: 170px 170px 40px 40px;
    background: linear-gradient(180deg, var(--glass-top) 0%, var(--glass-mid) 55%, var(--glass-base) 100%);
  }
  .offers {
    position: absolute;
    top: 640px;
    left: 0;
    width: 848px;
    list-style: none;
  }
  .offer {
    position: relative;
    height: 94px;
    font-size: 72px;
    line-height: 94px;
  }
  .offer__name { position: absolute; right: 340px; white-space: nowrap; }
  .offer__price { position: absolute; right: 98px; white-space: nowrap; }
  .contact {
    position: absolute;
    top: 1130px;
    left: 0;
    width: 848px;
    text-align: center;
    font-family: "Raleway", sans-serif;
  }
  .contact__details { font-size: 17px; line-height: 26px; }
  .contact__web { font-size: 20px; line-height: 28px; }
</style>
</head>
<body>
<main class="flyer">
  <svg class="backdrop" width="848" height="1200" viewBox="0 0 848 1200" aria-hidden="true">
    <path d="M0 0 H848 V525 C600 480 300 540 0 1090 Z" fill="var(--peach)"/>
  </svg>

  <div class="brand">Bramble Toots</div>

  <div class="rule rule--top"></div>
  <h1 class="title">Aperitivo</h1>
  <div class="rule rule--bottom"></div>
  <p class="hours">From 4pm - 6pm every day</p>

  <div class="cocktail-art" role="img" aria-label="Illustration of a stemmed coupe cocktail glass filled with a purple-to-red drink"></div>

  <ul class="offers">
    <li class="offer"><span class="offer__name">Negronis</span><span class="offer__price">$16</span></li>
    <li class="offer"><span class="offer__name">Vellaro Spritz</span><span class="offer__price">$14</span></li>
    <li class="offer"><span class="offer__name">All share plates</span><span class="offer__price">$10</span></li>
  </ul>

  <footer class="contact">
    <p class="contact__details">Address: 472 Wexcombe Rd, Wexcombe&nbsp; Phone: 8153 2947</p>
    <p class="contact__web">brambletoots.com.au</p>
  </footer>
</main>
</body>
</html>
```